Very Simple/Minimal Business Card Design Project

The company operates in the industrial maritime infrastructure sector in Brazil. You can find more information on our website www.navortek.com.br WE NEED TO LOOK POWERFUL AND SERIOUS
I have attached a copy of the old cards. We would like something more professional / industrial / sexy that also includes the position.

The card can be double sided or not. We would like you to propose as many options.

Thank you
Updates

Many thanks, do let me know if you have any questions. I am under a lot of time pressure to try and have them printed over the next days or so.

Please could you use the following information

for the address: Rua Tapiraçu, 417 - Centro, Rio de Janeiro, 20034-118, Brasil

for the mobile: +55 21 8237 9412
for the landline: +55 21 4096 3578

and position:  Diretor Geral

Thakn you

Target Market(s)

Shipowners, bankers, industrial companies

Industry/Entity Type

Industrial

Requirements
Must have
• POWERFUL
SERIOUS
SOLID
BIG CORPORATION

```html
<!DOCTYPE html>
<html lang="pt-BR">
<head>
<meta charset="utf-8">
<title>Navortek – Cartão de Visita</title>
<link rel="stylesheet" href="https://fonts.googleapis.com/css2?family=Roboto:wght@300;400;700&display=swap">
<style>
  :root {
    --backdrop: #1a1a1a;
    --card: #ffffff;
    --pattern-light: #f4f4f3;
    --pattern-dark: #e9e9e7;
    --brand-blue: #2b3990;
    --brand-green: #2e9a48;
    --ink: #3a3a3a;
    --ink-soft: #5a5a5a;
  }
  * { margin: 0; padding: 0; box-sizing: border-box; }
  html, body {
    width: 1200px; height: 800px; overflow: hidden;
    background: var(--backdrop);
    font-family: "Roboto", "Helvetica Neue", Arial, sans-serif;
  }
  .stage {
    position: relative; width: 1200px; height: 800px;
    display: flex; justify-content: center; align-items: center; gap: 60px;
  }
  .card {
    position: relative; width: 300px; height: 525px;
    background: var(--card);
    box-shadow: 0 10px 30px rgba(0,0,0,0.5);
  }
  /* Front */
  .card-front__pattern {
    position: absolute; inset: 0;
    background: linear-gradient(160deg, var(--pattern-light), var(--pattern-dark));
  }
  .card-front__brand {
    position: absolute; left: 36px; top: 232px;
    display: flex; align-items: center; gap: 8px;
  }
  .brand-square { width: 18px; height: 18px; background: var(--brand-green); }
  .brand-name {
    font-weight: 700; font-size: 24px; letter-spacing: 0.5px;
    color: var(--brand-blue);
  }
  /* Back */
  .card-back__brand {
    position: absolute; left: 32px; top: 150px;
    display: flex; align-items: center; gap: 10px;
  }
  .card-back__brand .brand-square { width: 26px; height: 26px; }
  .card-back__brand .brand-name { font-size: 32px; }
  .holder {
    position: absolute; left: 100px; top: 240px;
  }
  .holder__name { font-weight: 300; font-size: 25px; color: var(--ink); }
  .holder__role { font-size: 10px; color: var(--ink); margin-top: 2px; }
  .holder__icon { position: absolute; left: -22px; top: 8px; }
  .contacts {
    position: absolute; left: 100px; top: 312px;
    list-style: none; font-weight: 300; font-size: 14px; color: var(--ink-soft);
    line-height: 19px;
  }
  .contacts li { position: relative; }
  .contacts svg { position: absolute; left: -22px; top: 3px; }
  .contacts .address { margin-top: 14px; line-height: 19px; }
</style>
</head>
<body>
<main class="stage">
  <section class="card card-front" aria-label="Frente do cartão">
    <div class="card-front__pattern" role="img" aria-label="Padrão decorativo suave de triângulos em cinza claro"></div>
    <div class="card-front__brand">
      <span class="brand-square"></span>
      <span class="brand-name">NAVORTEK</span>
    </div>
  </section>

  <section class="card card-back" aria-label="Verso do cartão">
    <div class="card-back__brand">
      <span class="brand-square"></span>
      <span class="brand-name">NAVORTEK</span>
    </div>

    <div class="holder">
      <svg class="holder__icon" width="14" height="14" viewBox="0 0 14 14" aria-hidden="true">
        <circle cx="7" cy="4.5" r="3.2" fill="var(--brand-green)"/>
        <path d="M1 14c0-3.5 2.7-5.5 6-5.5s6 2 6 5.5z" fill="var(--brand-green)"/>
      </svg>
      <div class="holder__name">Rafael Monteiro</div>
      <div class="holder__role">Diretor Geral</div>
    </div>

    <ul class="contacts">
      <li>
        <svg width="13" height="13" viewBox="0 0 14 14" aria-hidden="true"><path d="M3 1l2.5 3-1.5 1.5c.8 1.8 2.2 3.2 4 4L9.5 8 13 10.5 11.5 13C6 12.5 1.5 8 1 2.5z" fill="var(--brand-green)"/></svg>
        +55 21 8237 9412
      </li>
      <li>
        <svg width="13" height="13" viewBox="0 0 14 14" aria-hidden="true"><path d="M1 5c2-3 10-3 12 0l-2 1.5-2-1V4H5v1.5l-2 1z" fill="var(--brand-green)"/><rect x="3" y="7" width="8" height="6" rx="1" fill="var(--brand-green)"/></svg>
        +55 21 4096 3578
      </li>
      <li>
        <svg width="13" height="13" viewBox="0 0 14 14" aria-hidden="true"><rect x="1" y="3" width="12" height="9" fill="var(--brand-green)"/><path d="M1 3l6 5 6-5" stroke="#fff" stroke-width="1.2" fill="none"/></svg>
        rafael@navortek.com.br
      </li>
      <li>
        <svg width="13" height="13" viewBox="0 0 14 14" aria-hidden="true"><circle cx="5.5" cy="5.5" r="3.8" stroke="var(--brand-green)" stroke-width="2" fill="none"/><path d="M8.5 8.5L13 13" stroke="var(--brand-green)" stroke-width="2.4"/></svg>
        http://www.navortek.com.br
      </li>
      <li class="address">
        <svg width="13" height="13" viewBox="0 0 14 14" aria-hidden="true"><path d="M7 1L1 7h2v6h3V9h2v4h3V7h2z" fill="var(--brand-green)"/></svg>
        Rua Tapiraçu, 417 - Centro<br>
        Rio de Janeiro, 20034-118<br>
        Brasil
      </li>
    </ul>
  </section>
</main>
</body>
</html>
```